Criação de Papelaria (6 itens) para Brisa & Lajedo
" Prestamos serviços de outorga e licenças ambientais, análise de água, aproveitamento de águas, pesquisa de água mineral, poços artesianos (furação, recuperação, tratamento de água), energia solar, etc. "

```html
<!DOCTYPE html>
<html lang="pt-BR">
<head>
<meta charset="UTF-8">
<title>Brisa &amp; Lajedo — Adesivo</title>
<link rel="stylesheet" href="https://fonts.googleapis.com/css2?family=Montserrat:wght@400;500;600&display=swap">
<style>
  :root {
    --page-grey: #c3c4c6;
    --sticker-white: #ffffff;
    --brand-blue: #2d5b96;
    --brand-green: #6e8f3f;
    --ink-dark: #3a3a3a;
    --ink-grey: #555a60;
  }
  html, body {
    margin: 0;
    padding: 0;
    width: 1200px;
    height: 1200px;
    overflow: hidden;
    background: var(--page-grey);
  }
  .canvas {
    position: relative;
    width: 1200px;
    height: 1200px;
    background: var(--page-grey);
    font-family: "Montserrat", sans-serif;
  }
  .sticker {
    position: absolute;
    left: 389px;
    top: 389px;
    width: 422px;
    height: 422px;
    box-sizing: border-box;
    border-radius: 50%;
    border: 12px solid var(--brand-blue);
    background: var(--sticker-white);
    box-shadow: 0 2px 6px rgba(0, 0, 0, 0.12);
  }
  .brand-name {
    position: absolute;
    left: 0;
    width: 1200px;
    top: 522px;
    margin: 0;
    text-align: center;
    font-size: 46px;
    font-weight: 600;
    line-height: 1;
    color: var(--brand-blue);
    letter-spacing: -0.5px;
  }
  .brand-tagline {
    position: absolute;
    left: 0;
    width: 1200px;
    top: 604px;
    margin: 0;
    text-align: center;
    font-size: 23px;
    font-weight: 400;
    line-height: 1;
    letter-spacing: 1.5px;
    color: var(--ink-dark);
  }
  .contact-phones {
    position: absolute;
    left: 0;
    width: 1200px;
    top: 660px;
    margin: 0;
    text-align: center;
    font-size: 17px;
    line-height: 22px;
    color: var(--ink-dark);
  }
  .website-arc {
    position: absolute;
    left: 0;
    top: 0;
    width: 1200px;
    height: 1200px;
  }
  .website-arc text {
    font-family: "Montserrat", sans-serif;
    font-size: 17px;
    letter-spacing: 4px;
    fill: var(--ink-grey);
  }
</style>
</head>
<body>
  <main class="canvas">
    <div class="sticker"></div>
    <h1 class="brand-name">Brisa &amp; Lajedo</h1>
    <p class="brand-tagline">SOLUÇÕES AMBIENTAIS</p>
    <p class="contact-phones">(00) 0000-0000<br>(00) 00000-0000</p>
    <svg class="website-arc" viewBox="0 0 1200 1200" aria-label="www.siteexempl.com.br">
      <defs>
        <path id="lower-arc" d="M 432 640 A 170 170 0 0 0 768 640"/>
      </defs>
      <text text-anchor="middle">
        <textPath href="#lower-arc" startOffset="50%">www.siteexempl.com.br</textPath>
      </text>
    </svg>
  </main>
</body>
</html>
```